Online homewares store needs a web design

We need a web design for a new high-end online homewares store. We are starting small with only 5 major categories.

Rugs
Bathe
Dine
Decorative
Sleep

This is just for design. No coding needed.

Please make high-end, sophisticated and minimal.

I have included some pictures to give you an idea of the products. I would like to showcase some of the pictures on the web page.

The website will be using an e-commerce function.

I have included the logo parlour nine hopes.

I like this website
http://marblewindowhouse.example/

or

brinqlotvane.example.au

Simple but effective - not too busy
Updates

Project Deadline Extended
Reason: I would like to extend my deadline to give designers more time to do quality work - as requested!! Thanks.

Target Market(s)

Females in the age bracket of 25-45

Males who are very house proud 25-45

Industry/Entity Type

Store

Requirements
Must have
• Upmarket

```html
<!DOCTYPE html>
<html lang="en">
<head>
<meta charset="utf-8">
<title>parlour nine hopes — homewares</title>
<link rel="stylesheet" href="https://fonts.googleapis.com/css2?family=Roboto:wght@300;400&display=swap">
<style>
  :root {
    --ink: #2b2b2b;
    --muted: #555555;
    --label: #7a7a7a;
    --rule: #d6d6d6;
    --rule-strong: #222222;
    --icon: #6a6a6a;
    --page: #ffffff;
    --hero-bg: linear-gradient(135deg, #3a2f2c 0%, #c9a98a 45%, #d0b79c 55%, #3b302d 100%);
  }
  * { margin: 0; padding: 0; box-sizing: border-box; }
  html, body {
    width: 842px; height: 1200px; overflow: hidden;
    background: var(--page);
    font-family: "Roboto", Arial, sans-serif;
    font-weight: 300;
    color: var(--ink);
  }
  .page { position: relative; width: 842px; height: 1200px; }

  .utility-bar {
    position: absolute; top: 21px; left: 61px; width: 720px;
    display: flex; justify-content: space-between; align-items: center;
    font-size: 10.5px; color: var(--muted); font-weight: 400;
  }
  .utility-bar .account-links span { margin: 0 5px; }
  .utility-bar .cart { display: flex; align-items: center; gap: 6px; }
  .rule-top { position: absolute; top: 55px; left: 61px; width: 720px; border-top: 1px solid var(--rule); }

  .brand {
    position: absolute; top: 78px; left: 0; width: 842px; text-align: center;
    font-size: 46px; font-weight: 300; letter-spacing: -1.5px; color: var(--ink);
  }

  .main-nav {
    position: absolute; top: 157px; left: 61px; width: 720px; height: 46px;
    border-top: 1px solid var(--rule); border-bottom: 2px solid var(--rule-strong);
    display: flex; align-items: center;
  }
  .main-nav .home { width: 80px; display: flex; justify-content: center; }
  .main-nav ul { list-style: none; display: flex; flex: 1; }
  .main-nav li {
    flex: auto; text-align: center; font-size: 12.5px; font-weight: 400;
    border-left: 1px solid #9a9a9a; line-height: 18px; letter-spacing: -0.2px;
  }

  .hero {
    position: absolute; top: 219px; left: 61px; width: 720px; height: 388px;
    background: var(--hero-bg);
  }
  .hero .arrow { position: absolute; top: 158px; }
  .hero .arrow.prev { left: 0; }
  .hero .arrow.next { right: 0; }

  .category-grid {
    position: absolute; top: 658px; left: 61px; width: 720px;
    display: grid; grid-template-columns: repeat(3, 220px); column-gap: 30px; row-gap: 46px;
  }
  .category .photo { width: 220px; height: 156px; }
  .category .name {
    text-align: center; font-size: 18px; line-height: 22px; color: var(--label);
    margin-top: 10px; letter-spacing: -0.3px;
  }
  .photo.rugs { background: linear-gradient(160deg, #d9a88e, #c9477a 60%, #3c7fa8); }
  .photo.bathe { background: linear-gradient(160deg, #e8e2da, #b33b5c 50%, #3a6fb0); }
  .photo.dine { background: linear-gradient(160deg, #f2f0ea, #d9a26d 50%, #e9b54a); }
  .photo.decorative { background: linear-gradient(160deg, #f1efec, #e6e2de 60%, #d9607d); }
  .photo.sleep { background: linear-gradient(160deg, #e7e4e0, #4f9e86 55%, #2f7f74); }
  .photo.cushion { background: linear-gradient(160deg, #d8b158, #c06048 50%, #6c9aa8); border: 1px solid #cfcfcf; }

  .site-footer {
    position: absolute; top: 1125px; left: 61px; width: 721px;
    border-top: 1px solid var(--rule);
    display: flex; justify-content: space-between; align-items: center;
    padding-top: 26px;
  }
  .site-footer .copyright { font-size: 10.5px; color: var(--muted); font-weight: 400; }
  .social { display: flex; gap: 8px; margin-top: -4px; }
  .social .share-link {
    width: 29px; height: 29px; border: 1.5px solid #8a8a8a; border-radius: 50%;
    display: flex; align-items: center; justify-content: center;
  }
</style>
</head>
<body>
<div class="page">
  <header>
    <div class="utility-bar">
      <div class="account-links">REGISTER<span>|</span>LOGIN<span>|</span>MY ACCOUNT</div>
      <div class="cart">
        <svg width="13" height="12" viewBox="0 0 13 12" aria-hidden="true">
          <path d="M0.5 1h2l1.6 6.5h7l1.4-4.5H3.2" fill="none" stroke="#555" stroke-width="1.1"/>
          <circle cx="5" cy="10" r="1" fill="#555"/><circle cx="10" cy="10" r="1" fill="#555"/>
        </svg>
        CART (0) ITEMS
      </div>
    </div>
    <div class="rule-top"></div>
    <div class="brand">parlour nine hopes</div>
    <nav class="main-nav">
      <div class="home">
        <svg width="24" height="22" viewBox="0 0 24 22" aria-label="Home">
          <path d="M12 1L1 11h3v10h6v-6h4v6h6V11h3z" fill="#111"/>
        </svg>
      </div>
      <ul>
        <li>ABOUT US</li><li>PRODUCTS</li><li>SHOP</li><li>STOCKISTS</li><li>CATALOGUE</li><li>CONTACT US</li>
      </ul>
    </nav>
  </header>

  <section class="hero" role="img" aria-label="Round jute rug ringed with colourful felt circles on a dark carpet">
    <svg class="arrow prev" width="28" height="56" viewBox="0 0 28 56" aria-hidden="true">
      <path d="M0 0L28 28L0 56z" fill="#fff"/>
      <path d="M9 21L3 28L9 35" fill="none" stroke="#333" stroke-width="1"/>
    </svg>
    <svg class="arrow next" width="28" height="56" viewBox="0 0 28 56" aria-hidden="true">
      <path d="M28 0L0 28L28 56z" fill="#fff"/>
      <path d="M19 21L25 28L19 35" fill="none" stroke="#333" stroke-width="1"/>
    </svg>
  </section>

  <main class="category-grid">
    <div class="category"><div class="photo rugs" role="img" aria-label="Child's bare feet on a colourful felt ball rug"></div><div class="name">RUGS</div></div>
    <div class="category"><div class="photo bathe" role="img" aria-label="Folded striped bath towels with tassels and soap"></div><div class="name">BATHE</div></div>
    <div class="category"><div class="photo dine" role="img" aria-label="Stacked wooden boards with colour-dipped ends"></div><div class="name">DINE</div></div>
    <div class="category"><div class="photo decorative" role="img" aria-label="White decorative figure with strings of felt beads"></div><div class="name">DECORATIVE</div></div>
    <div class="category"><div class="photo sleep" role="img" aria-label="Bed with green patterned quilt and pink side table"></div><div class="name">SLEEP</div></div>
    <div class="category"><div class="photo cushion" role="img" aria-label="Stack of round patchwork floor cushions"></div><div class="name">CUSHION</div></div>
  </main>

  <footer class="site-footer">
    <div class="copyright">Copyright © 2013. All Rights Reserved.</div>
    <div class="social" aria-label="Share and follow">
      <span class="share-link" aria-label="Message">
        <svg width="14" height="13" viewBox="0 0 14 13" aria-hidden="true">
          <path d="M1.5 1.5h11v7h-6l-3 3v-3h-2z" fill="none" stroke="var(--icon)" stroke-width="1.3" stroke-linejoin="round"/>
        </svg>
      </span>
      <span class="share-link" aria-label="Email">
        <svg width="14" height="11" viewBox="0 0 14 11" aria-hidden="true">
          <rect x="1" y="1" width="12" height="9" fill="none" stroke="var(--icon)" stroke-width="1.3"/>
          <path d="M1 1.5l6 4.5 6-4.5" fill="none" stroke="var(--icon)" stroke-width="1.3"/>
        </svg>
      </span>
      <span class="share-link" aria-label="Favourite">
        <svg width="14" height="13" viewBox="0 0 14 13" aria-hidden="true">
          <path d="M7 11.5L1.8 6.4A2.9 2.9 0 0 1 7 2.6a2.9 2.9 0 0 1 5.2 3.8z" fill="none" stroke="var(--icon)" stroke-width="1.3" stroke-linejoin="round"/>
        </svg>
      </span>
      <span class="share-link" aria-label="Share">
        <svg width="13" height="13" viewBox="0 0 13 13" aria-hidden="true">
          <circle cx="3" cy="6.5" r="1.8" fill="var(--icon)"/>
          <circle cx="10" cy="2.5" r="1.8" fill="var(--icon)"/>
          <circle cx="10" cy="10.5" r="1.8" fill="var(--icon)"/>
          <path d="M3 6.5L10 2.5M3 6.5L10 10.5" stroke="var(--icon)" stroke-width="1.2"/>
        </svg>
      </span>
    </div>
  </footer>
</div>
</body>
</html>
```